Upmarket Dessert Lounge needs a Business Card Design

We are an upmarket dessert lounge needing a business card to match our image.

We want something that is simple yet beautiful, feminine, classy, sophisticated and elegant. We want it to stand out and don't mind if it is bold.

The design should include our logo and colours of red or maroon with gold highlights. We don't mind if black is used.

Marlow & Quince

Target Market(s)

For those who like to indulge or treat themselves and give in to their temptations on good quality desserts.

Industry/Entity Type

Business

Requirements
Must have
• Must include our logo and our name

Marlow & Quince

M & Q

```html
<!DOCTYPE html>
<html lang="en">
<head>
<meta charset="utf-8">
<title>Marlow &amp; Quince – Business Card</title>
<link rel="stylesheet" href="https://fonts.googleapis.com/css2?family=Cinzel:wght@500&family=Lora:wght@600&family=Open+Sans:wght@400&display=swap">
<style>
  :root {
    --page: #ecebe8;
    --maroon-light: #a3262a;
    --maroon: #8a1c20;
    --maroon-dark: #5e1013;
    --gold: #d9a878;
    --gold-soft: #c99566;
    --tan: #f6c58e;
    --tan-text: #6a2a18;
    --white: #ffffff;
    --cream-text: #fbefe4;
  }
  * { box-sizing: border-box; margin: 0; padding: 0; }
  html, body { width: 1200px; height: 951px; overflow: hidden; background: var(--page); }
  .canvas { position: relative; width: 1200px; height: 951px; }

  .card {
    position: absolute;
    width: 580px;
    height: 350px;
    border-radius: 24px;
    overflow: hidden;
    box-shadow: 0 10px 28px rgba(0,0,0,.18);
  }

  /* Front */
  .card-front {
    left: 80px; top: 110px;
    background: radial-gradient(ellipse at 40% 45%, var(--maroon-light) 0%, var(--maroon) 55%, var(--maroon-dark) 100%);
  }
  .corner-flourish {
    position: absolute; right: 0; top: 0;
    width: 300px; height: 80px;
  }
  .brand-name {
    position: absolute;
    left: 70px; top: 128px;
    width: 330px;
    text-align: center;
    font-family: "Cinzel", serif;
    font-weight: 500;
    font-size: 36px;
    letter-spacing: 1px;
    color: var(--gold);
  }
  .front-web {
    position: absolute;
    left: 80px; top: 262px;
    width: 330px;
    text-align: center;
    font-family: "Lora", serif;
    font-weight: 600;
    font-size: 17px;
    letter-spacing: 1px;
    color: var(--cream-text);
  }

  /* Back */
  .card-back {
    left: 540px; top: 500px;
    background: var(--white);
  }
  .info-band {
    position: absolute;
    left: 0; top: 62px;
    width: 100%; height: 158px;
    background: var(--tan);
  }
  .name-block {
    position: absolute;
    left: 0; top: 0;
    width: 232px; height: 100%;
    background: linear-gradient(90deg, var(--maroon-dark), var(--maroon-light) 60%, var(--maroon));
    display: flex; align-items: center; justify-content: center;
    font-family: "Open Sans", sans-serif;
    font-size: 22px;
    color: var(--white);
  }
  .divider {
    position: absolute;
    left: 254px; top: 30px;
    width: 1px; height: 80px;
    background: var(--tan-text);
  }
  .contact {
    position: absolute;
    left: 272px; top: 30px;
    list-style: none;
    font-family: "Open Sans", sans-serif;
    font-size: 15px;
    line-height: 20px;
    color: var(--tan-text);
  }
</style>
</head>
<body>
<main class="canvas">
  <section class="card card-front">
    <svg class="corner-flourish" viewBox="0 0 300 80" role="img" aria-label="Gold floral scroll ornament along the top edge">
      <defs>
        <linearGradient id="flourishTone" x1="0" x2="1">
          <stop offset="0" stop-color="#d9a878" stop-opacity="0.25"/>
          <stop offset="1" stop-color="#d9a878" stop-opacity="0.55"/>
        </linearGradient>
      </defs>
      <path d="M0 0 H300 V70 Q200 80 120 40 Q60 15 0 0 Z" fill="url(#flourishTone)"/>
    </svg>
    <div class="brand-name">MARLOW &amp; QUINCE</div>
    <div class="front-web">www.marlowquince.com</div>
  </section>

  <section class="card card-back">
    <div class="info-band">
      <div class="name-block">Marlow &amp; Quince</div>
      <span class="divider"></span>
      <ul class="contact">
        <li>ph. 512-555-0142</li>
        <li>fax 512-555-0143</li>
        <li>hello@marlowquince.com</li>
        <li>www.marlowquince.com</li>
      </ul>
    </div>
  </section>
</main>
</body>
</html>
```